Goodlooking website for a company who is working in the IT consultancy

We want a new website designed in WordPress. You can take www.vantorq.nl as an example. It should be a website with some short blocks of information about the company, nice pictures of our partners and our employees. A job page with a clear filter.

Target Market(s)

B2B

Industry/Entity Type

It Company

Coding

Coded - Design and coding required

Number of Pages Required

5+ page

Font styles to use
Sans Serif

Colors
0455a3
34a7d8

Requirements
Must have
• Check briefing

```html
<!DOCTYPE html>
<html lang="en">
<head>
<meta charset="utf-8">
<title>Vantorq – Our Solutions</title>
<link href="https://fonts.googleapis.com/css2?family=PT+Sans:wght@400;700&display=swap" rel="stylesheet">
<style>
:root{
  --brand:#34a7d8;
  --brand-dark:#0455a3;
  --ink:#222;
  --text:#444;
  --muted:#888;
  --page:#f6f6f6;
  --card:#f8f8f8;
  --footer:#333;
  --footer-line:#4a4a4a;
  --bottom:#3a3a3a;
}
*{box-sizing:border-box;margin:0;padding:0}
html,body{width:1057px;height:1200px;overflow:hidden}
body{font-family:'PT Sans',sans-serif;background:var(--page);color:var(--text);position:relative}
.site-header{position:absolute;top:0;left:0;width:1057px;height:60px;background:#fff;box-shadow:0 1px 3px rgba(0,0,0,.12);z-index:2}
.brand{position:absolute;left:170px;top:10px;display:flex;align-items:center;gap:8px}
.brand-dot{width:40px;height:40px;border-radius:50%;background:var(--brand)}
.brand-name{font-size:26px;font-weight:400;letter-spacing:3px;color:#2b3a44}
.main-nav{position:absolute;left:476px;top:0;display:flex;height:60px}
.main-nav a{display:block;height:60px;line-height:58px;padding:0 15px;font-size:8px;font-weight:700;text-transform:uppercase;color:#888;text-decoration:none;letter-spacing:.3px}
.main-nav a.active{background:var(--brand);color:#fff;padding:0 16px}
.page-hero{position:absolute;top:60px;left:0;width:1057px;height:82px;background:linear-gradient(90deg,#2f8fbd 0%,#3d9ccb 45%,#7fb6d6 100%)}
.page-hero h1{position:absolute;left:170px;top:29px;font-size:21px;font-weight:700;color:#fff}
.breadcrumb{position:absolute;top:142px;left:0;width:1057px;height:33px;background:#efefef;border-bottom:1px solid #e0e0e0;font-size:9px;font-weight:700;color:#333;padding:12px 0 0 170px;letter-spacing:.4px}
.card{position:absolute;width:340px;background:var(--card);box-shadow:0 0 4px rgba(0,0,0,.12);text-align:center;padding:0 24px}
.card-icon{width:56px;height:56px;border-radius:50%;background:var(--brand);margin:0 auto;display:flex;align-items:center;justify-content:center}
.card h2{font-size:12.5px;font-weight:700;color:var(--ink);margin:16px 0 9px}
.card p{font-size:9px;line-height:16px;color:var(--text)}
.cta{position:absolute;top:677px;left:0;width:1057px;height:175px;background:linear-gradient(110deg,#1d4b6e 0%,#173f5d 50%,#0f2b40 100%);text-align:center;color:#fff}
.cta h2{font-size:20px;font-weight:400;margin-top:30px}
.cta p{font-size:9px;line-height:18px;margin:12px auto 0;width:480px;color:#dbe6ee}
.cta-btn{display:inline-flex;align-items:center;gap:5px;margin-top:14px;background:var(--brand);color:#fff;border-radius:16px;height:30px;padding:0 13px;font-size:9px;font-weight:700;text-transform:uppercase;letter-spacing:.4px;box-shadow:0 2px 0 #1e7ea8}
.site-footer{position:absolute;top:852px;left:0;width:1057px;height:285px;background:var(--footer);color:#bbb}
.footer-col{position:absolute;top:46px}
.footer-col h3{font-size:13px;font-weight:400;color:#fff;letter-spacing:1px;padding-bottom:10px;border-bottom:1px solid var(--footer-line);position:relative}
.footer-col h3::after{content:"";position:absolute;left:0;bottom:-1px;width:29px;height:2px;background:var(--brand)}
.info-item{position:relative;padding-left:22px;margin-top:20px;font-size:10px;letter-spacing:.6px;line-height:15px}
.info-item svg{position:absolute;left:0;top:1px}
.info-item strong{color:#fff;display:block;margin-bottom:3px}
.info-item .big{font-size:13px;color:#ccc}
.info-item .link{font-size:13px;color:var(--brand)}
.link-list{list-style:none;margin-top:10px}
.link-list li{font-size:9.5px;letter-spacing:.8px;color:#bbb;height:27px;line-height:27px;border-bottom:1px solid #3c3c3c;padding-left:18px;position:relative}
.link-list li:last-child{border-bottom:none}
.link-list li::before{content:"»";position:absolute;left:0;color:#888}
.newsletter p{font-size:9px;color:#999;margin-top:20px}
.email-field{margin-top:12px;width:190px;height:26px;background:#fff;border:1px solid #ccc;font-size:9px;color:#999;padding:7px 9px}
.subscribe{margin-top:11px;display:inline-flex;align-items:center;gap:6px;height:26px;padding:0 15px;border-radius:13px;background:#4a4a4a;color:#fff;font-size:9.5px}
.bottom-bar{position:absolute;top:1137px;left:0;width:1057px;height:63px;background:var(--bottom);text-align:center}
.social{display:flex;justify-content:center;gap:5px;margin-top:11px}
.social span{width:26px;height:26px;border-radius:50%;border:1px solid #777}
.copyright{font-size:8px;color:#888;letter-spacing:.8px;margin-top:8px}
</style>
</head>
<body>
<header class="site-header">
  <div class="brand"><span class="brand-dot"></span><span class="brand-name">VANTORQ</span></div>
  <nav class="main-nav">
    <a href="#">Home</a><a href="#" class="active">Our Solutions</a><a href="#">Our Team</a><a href="#">Jobs</a><a href="#">News/Blog</a><a href="#">Contact</a>
  </nav>
</header>

<section class="page-hero" role="img" aria-label="Blue-tinted photo of glass office towers">
  <h1>Our Solutions</h1>
</section>
<div class="breadcrumb">Home &gt; Our Solutions</div>

<article class="card" style="left:179px;top:210px;height:211px;padding-top:22px">
  <div class="card-icon"><svg width="28" height="22" viewBox="0 0 28 22" fill="none" stroke="#fff" stroke-width="2"><rect x="5" y="2" width="18" height="13" rx="1"/><path d="M2 18h24" stroke-linecap="round"/></svg></div>
  <h2>Automation &amp; Deployment</h2>
  <p>Vantorq can provide you with advice, describing the required architecture as well as providing high-quality consultancy where the consultant realizes and / or supervises the implementation in collaboration with the internal technicians and can also provide the necessary training.</p>
</article>

<article class="card" style="left:538px;top:210px;height:211px;padding-top:19px">
  <div class="card-icon"><svg width="26" height="26" viewBox="0 0 26 26" fill="#fff"><path d="M22 4c-6 0-10 3-13 8l5 5c5-3 8-7 8-13z"/><path d="M9 12l-5 1 3-4 4-1zM14 17l-1 5 4-3 1-4z"/><path d="M7 16l3 3-5 3z"/></svg></div>
  <h2>Mission Critical Solutions</h2>
  <p>Vantorq is the specialist in the construction and management of Mission Critical Systems. Our Mission Critical team can design IT environments for you that are fully operational 24 hours a day, 365 days a year. This means that we design and build systems that achieve up to 100 percent up-time and ensure that your IT environment is always available.</p>
</article>

<article class="card" style="left:179px;top:440px;height:202px;padding-top:22px">
  <div class="card-icon"><svg width="32" height="22" viewBox="0 0 32 22" fill="#fff"><path d="M8 21a6 6 0 0 1-1-12 8 8 0 0 1 15-2 6 6 0 0 1 3 14z"/></svg></div>
  <h2>Cloud Consultancy</h2>
  <p>Vantorq provides consultancy for both private and public cloud environments. We support this through professional advice and also have concepts that can help you realize a hybrid environment. Also providing a complete "Cloud-based Storage environment" is part of our service.</p>
</article>

<article class="card" style="left:538px;top:440px;height:202px;padding-top:22px">
  <div class="card-icon"><svg width="30" height="24" viewBox="0 0 30 24" fill="#fff"><rect x="1" y="1" width="8" height="6" rx="1"/><rect x="11" y="1" width="8" height="6" rx="1"/><rect x="21" y="1" width="8" height="6" rx="1"/><rect x="1" y="9" width="8" height="6" rx="1"/><rect x="11" y="9" width="8" height="6" rx="1"/><rect x="21" y="9" width="8" height="6" rx="1"/><rect x="1" y="17" width="8" height="6" rx="1"/><rect x="11" y="17" width="8" height="6" rx="1"/><rect x="21" y="17" width="8" height="6" rx="1"/></svg></div>
  <h2>Hyperconverged Infrastructures</h2>
  <p>Among other things, Vantorq supplies Nexagrid products in which computing power, storage and networks are fully integrated and in which you form a complete data center through virtualisation. This can also be installed on certified hardware such as Corvano, Altex or Veltron Systems.</p>
</article>

<section class="cta">
  <h2>Start Your Free Consultation</h2>
  <p>I am text block. Click edit button to change this text. Lorem ipsum dolor sit amet, consectetur adipiscing elit. Ut elit tellus, luctus nec ullamcorper mattis, pulvinar dapibus leo.</p>
  <span class="cta-btn">Contact Us <svg width="9" height="9" viewBox="0 0 10 10" fill="none" stroke="#fff" stroke-width="1.4"><circle cx="5" cy="5" r="4"/><path d="M3.5 5h3M5.3 3.6 6.7 5 5.3 6.4"/></svg></span>
</section>

<footer class="site-footer">
  <div class="footer-col" style="left:188px;width:151px">
    <h3>Contact Info</h3>
    <div class="info-item"><svg width="10" height="13" viewBox="0 0 10 13" fill="#34a7d8"><path d="M5 0a5 5 0 0 0-5 5c0 4 5 8 5 8s5-4 5-8a5 5 0 0 0-5-5zm0 7a2 2 0 1 1 0-4 2 2 0 0 1 0 4z"/></svg><strong>Address:</strong>Keplerstraat 14,<br>3521 KL Utrecht</div>
    <div class="info-item"><svg width="11" height="11" viewBox="0 0 12 12" fill="#34a7d8"><path d="M2 0l2 3-1 2c1 2 2 3 4 4l2-1 3 2-1 2C5 12 0 7 0 2z"/></svg><strong>Phone:</strong><span class="big">085-2047316</span></div>
    <div class="info-item"><svg width="12" height="9" viewBox="0 0 12 9" fill="#34a7d8"><path d="M0 0h12v1L6 5 0 1zM0 2l6 4 6-4v7H0z"/></svg><strong>Email:</strong><span class="link">info@vantorq.nl</span></div>
  </div>
  <div class="footer-col" style="left:376px;width:110px">
    <h3>Quick Links</h3>
    <ul class="link-list"><li>Home</li><li>Our Solutions</li><li>Our Team</li><li>Jobs</li><li>Contact</li></ul>
  </div>
  <div class="footer-col" style="left:523px;width:118px">
    <h3>Support</h3>
    <ul class="link-list"><li>Terms of Use</li><li>Privacy Policy</li><li>Cookie Policy</li></ul>
  </div>
  <div class="footer-col newsletter" style="left:678px;width:190px">
    <h3>Join Our Newsletter</h3>
    <p>Subscribe for Job Alerts and Updates!</p>
    <div class="email-field">Enter Your Email</div>
    <span class="subscribe"><svg width="10" height="10" viewBox="0 0 10 10" fill="#fff"><path d="M10 0 0 4l3 1 1 4 2-3 3 2z"/></svg>Subscribe</span>
  </div>
</footer>

<div class="bottom-bar">
  <div class="social"><span></span><span></span></div>
  <p class="copyright">Copyright © 2018 VANTORQ. All Rights Reserved.</p>
</div>
</body>
</html>
```